WEBSITE NEEDED FOR MY COMPANY CALLED BRAMWORTH HOCKEY DEVELOPMENT

LOOKING FOR A WEBSITE TO MARKET AND SEEL MY HOCKEY DEVELOPMENT PROGRAMS.
NEEDS TO HAVE 5+ PAGES

Target Market(s)

YOUTH SPORTS

Industry/Entity Type

YOUTH ATHLETE DEVELOPMENT

Number of Pages Required

5+ page

Font styles to use
Sans Serif

Colors
0054AA
0677BA
7BADD7
CADEEF
E8F1F8

Requirements
Must have
• MAIN PAGE - SPIRNG PROGRAM PAGE - SUMMER PROGRAM PAGE - WINTER PAGE - TOURNAMENT PAGE
Nice to have
• FLASH
Should not have
• NOT SURE

```html
<!DOCTYPE html>
<html lang="en">
<head>
<meta charset="utf-8">
<title>Bramworth Hockey Development</title>
<link href="https://fonts.googleapis.com/css2?family=Audiowide&family=Barlow:wght@500;600;700;800&family=Exo+2:ital,wght@0,400;1,800&family=Mulish:wght@400;500&display=swap" rel="stylesheet">
<style>
:root{
  --cyan:#1fb0ec;
  --cyan-dark:#0e8fd0;
  --navy:#0f1c2e;
  --navy-deep:#0a1422;
  --ink:#1c2330;
  --text:#3c4452;
  --white:#ffffff;
  --ice:#eef5fa;
}
*{box-sizing:border-box;margin:0;padding:0}
html,body{width:1200px;height:3407px;overflow:hidden}
body{font-family:"Mulish",sans-serif;color:var(--text);background:var(--white)}
.page{position:relative;width:1200px;height:3407px;overflow:hidden}
.abs{position:absolute}
a{color:inherit;text-decoration:none}

/* header */
.site-header{position:absolute;left:0;top:0;width:1200px;height:80px;background:var(--white);z-index:5}
.brand{position:absolute;left:82px;top:0;width:220px;height:93px;z-index:6}
.brand-name{position:absolute;left:0;top:10px;width:220px;text-align:center;font-family:"Barlow",sans-serif;font-weight:800;font-size:21px;line-height:23px;color:var(--cyan)}
.main-nav a{position:absolute;top:28px;font-family:"Barlow",sans-serif;font-weight:500;font-size:15px;color:var(--ink);letter-spacing:.2px}
.main-nav a.active{font-weight:700}
.nav-underline{left:352px;top:53px;width:138px;height:2px;background:var(--cyan)}
.nav-divider{left:1054px;top:27px;width:1px;height:20px;background:#cfd6de}

/* hero */
.hero{left:0;top:80px;width:1200px;height:601px}
.hero-kicker{left:122px;top:268px;font-family:"Exo 2",sans-serif;font-size:29px;letter-spacing:2px;color:var(--white)}
.hero-title{left:118px;top:304px;font-family:"Exo 2",sans-serif;font-style:italic;font-weight:800;font-size:44px;line-height:46px;color:var(--white);letter-spacing:1px;white-space:nowrap}
.btn-outline{display:flex;align-items:center;justify-content:center;border:3px solid var(--white);border-radius:26px;font-family:"Barlow",sans-serif;font-weight:700;font-size:14px;letter-spacing:2px;color:var(--white)}
.hero-btn{left:119px;top:459px;width:191px;height:48px}

/* about */
.about{left:607px;top:814px;width:560px}
.about-kicker{font-family:"Audiowide",sans-serif;font-size:19px;line-height:24px;color:var(--cyan)}
.about-title{margin-top:6px;font-family:"Audiowide",sans-serif;font-weight:400;font-size:32px;line-height:37px;color:var(--ink);white-space:nowrap}
.about-title span{color:var(--cyan)}
.about-rule{margin-top:10px;width:74px;height:3px;background:var(--cyan)}
.about-copy{margin-top:16px;width:500px;font-size:17.5px;line-height:27px;color:var(--ink)}
.btn-ink{display:flex;align-items:center;justify-content:center;border:3px solid var(--cyan);border-radius:26px;font-family:"Barlow",sans-serif;font-weight:700;font-size:14px;letter-spacing:2px;color:var(--ink)}
.about-btn{margin:26px 0 0 -4px;width:189px;height:48px}

/* season split */
.season{left:0;top:1257px;width:1200px;height:602px}
.season-block{position:absolute;width:440px;text-align:center;color:var(--white)}
.season-title{font-family:"Audiowide",sans-serif;font-weight:400;font-size:31px}
.season-rule{width:62px;height:3px;background:var(--white);margin:12px auto 14px}
.season-copy{font-size:17px;line-height:25px}
.season-btn{margin:22px auto 0;width:178px;height:46px}

/* program cards */
.section-title{position:absolute;left:0;width:1200px;text-align:center;font-family:"Audiowide",sans-serif;font-weight:400;font-size:36px;color:var(--ink)}
.section-title span{color:var(--cyan)}
.section-rule{position:absolute;left:573px;width:54px;height:3px;background:var(--cyan)}
.program-card{position:absolute;top:2014px;height:295px;overflow:hidden}
.program-card .caption{position:absolute;left:0;bottom:22px;width:100%;text-align:center;color:var(--white)}
.caption-title{font-family:"Barlow",sans-serif;font-weight:700;font-size:19px}
.caption-link{font-family:"Barlow",sans-serif;font-size:12px;text-decoration:underline;margin-top:2px;display:inline-block}
.program-feature{position:absolute;left:302px;top:1978px;width:296px;height:360px;border-radius:0 36px 0 36px;overflow:hidden;background:linear-gradient(180deg,#1b2f45 0%,#1a6fa8 45%,#1aa6e8 100%)}
.feature-body{position:absolute;left:0;top:108px;width:100%;text-align:center;color:var(--white)}
.feature-title{font-family:"Barlow",sans-serif;font-weight:700;font-size:19px}
.feature-copy{font-size:15px;line-height:19.5px;margin:10px auto 0;width:230px}
.feature-btn{margin:24px auto 0;width:139px;height:36px;font-size:12px;border-width:2px}

/* tournaments */
.tournament-bg{left:0;top:2341px;width:1200px;height:680px;background:linear-gradient(180deg,#ffffff 0%,#f3f7fb 35%,#e7eff6 65%,#f4f8fb 100%)}
.tournament-card{position:absolute;top:2516px;width:309px;height:392px;background:var(--white);border:1px solid #d5dbe2}
.tournament-card .photo{position:absolute;left:0;top:0;width:100%;height:213px}
.t-title{position:absolute;left:29px;top:244px;font-family:"Audiowide",sans-serif;font-weight:400;font-size:17px;color:var(--ink)}
.t-copy{position:absolute;left:29px;top:272px;width:255px;font-size:12.5px;line-height:18.5px;color:var(--text)}
.t-btn{position:absolute;left:29px;top:338px;width:130px;height:35px;background:var(--cyan);color:var(--white);font-family:"Audiowide",sans-serif;font-size:13px;display:flex;align-items:center;justify-content:center}

/* footer */
.footer-brand{left:150px;top:3106px;width:230px;font-family:"Barlow",sans-serif;font-weight:800;font-size:26px;line-height:27px;color:var(--cyan)}
.footer-about{left:150px;top:3202px;width:270px;font-size:12.5px;line-height:22px;color:#c9d2dd}
.footer-col{position:absolute;top:3112px}
.footer-col h4{font-family:"Audiowide",sans-serif;font-weight:400;font-size:14px;color:var(--white);letter-spacing:.5px;margin-bottom:14px}
.footer-col li{list-style:none;font-size:13px;line-height:29px;color:#d6dde6}
.footer-mark{position:absolute;top:3112px;width:3px;height:22px;background:var(--cyan)}
.footer-sep{position:absolute;top:3056px;width:1px;height:212px;background:#223247}
.social{position:absolute;top:3141px;width:28px;height:28px;border-radius:50%;background:var(--white)}
.copyright{left:0;top:3347px;width:1200px;height:60px;background:var(--navy-deep);text-align:center;line-height:60px;font-size:12.5px;color:#c9d2dd}
.copyright a{color:var(--white);text-decoration:underline}
</style>
</head>
<body>
<div class="page">

  <!-- HEADER -->
  <header class="site-header">
    <nav class="main-nav">
      <a class="active" href="#" style="left:355px">SPIRNG PROGRAM</a>
      <a href="#" style="left:531px">SUMMER PROGRAM</a>
      <a href="#" style="left:713px">WINTER</a>
      <a href="#" style="left:815px">TOURNAMENT</a>
      <a href="#" style="left:961px">CONTACT</a>
    </nav>
    <div class="abs nav-underline"></div>
    <div class="abs nav-divider"></div>
    <svg class="abs" style="left:1075px;top:26px" width="24" height="24" viewBox="0 0 24 24" aria-label="Search">
      <circle cx="10" cy="10" r="7.5" fill="none" stroke="#1fb0ec" stroke-width="2"/>
      <line x1="15.5" y1="15.5" x2="22" y2="22" stroke="#1fb0ec" stroke-width="2" stroke-linecap="round"/>
    </svg>
  </header>
  <div class="brand">
    <svg class="abs" style="left:0;top:0" width="220" height="93" viewBox="0 0 220 93" aria-hidden="true">
      <polygon points="0,0 220,0 220,80 207,93 13,93 0,80" fill="#ffffff"/>
    </svg>
    <div class="brand-name">BRAMWORTH<br>HOCKEY<br>DEVELOPMENT</div>
  </div>

  <!-- HERO -->
  <section class="abs hero">
    <svg class="abs" style="left:0;top:0" width="1200" height="601" viewBox="0 0 1200 601" aria-hidden="true">
      <defs>
        <linearGradient id="heroLeft" x1="0" y1="0" x2="1" y2="0.6">
          <stop offset="0" stop-color="#0c2a48"/>
          <stop offset="0.45" stop-color="#126aa6"/>
          <stop offset="1" stop-color="#1cb2f0"/>
        </linearGradient>
      </defs>
      <rect width="1200" height="601" fill="url(#heroLeft)"/>
    </svg>
    <svg class="abs" style="left:0;top:0" width="1200" height="601" viewBox="0 0 1200 601" role="img" aria-label="Two hockey players facing off on the ice under arena lights">
      <defs>
        <linearGradient id="heroPhoto" x1="0" y1="0" x2="0" y2="1">
          <stop offset="0" stop-color="#3a4a66"/>
          <stop offset="0.45" stop-color="#7e91ab"/>
          <stop offset="1" stop-color="#c9d7e4"/>
        </linearGradient>
      </defs>
      <polygon points="715,0 1200,0 1200,601 503,601" fill="url(#heroPhoto)"/>
    </svg>
    <svg class="abs" style="left:36px;top:256px" width="26" height="46" viewBox="0 0 26 46" aria-label="Previous slide"><polyline points="22,4 6,23 22,42" fill="none" stroke="#fff" stroke-width="6"/></svg>
    <svg class="abs" style="left:1148px;top:256px" width="26" height="46" viewBox="0 0 26 46" aria-label="Next slide"><polyline points="4,4 20,23 4,42" fill="none" stroke="#fff" stroke-width="6"/></svg>
  </section>
  <div class="abs hero-kicker">WELCOME TO</div>
  <h1 class="abs hero-title">BRAMWORTH HOCKEY<br>DEVELOPMENT<br>PROGRAMS</h1>
  <a class="abs btn-outline hero-btn" href="#">VIEW PROGRAM</a>

  <!-- ABOUT -->
  <svg class="abs" style="left:120px;top:740px" width="432" height="497" viewBox="120 740 432 497" role="img" aria-label="Hockey goalie in red jersey crouched in a hexagon frame">
    <defs>
      <radialGradient id="goalie" cx="0.5" cy="0.45" r="0.6">
        <stop offset="0" stop-color="#5a6f86"/>
        <stop offset="0.6" stop-color="#22344a"/>
        <stop offset="1" stop-color="#0f1a28"/>
      </radialGradient>
    </defs>
    <polygon points="337,747 546,867 546,1111 337,1230 126,1111 126,867" fill="none" stroke="#1fb0ec" stroke-width="2"/>
    <polygon points="337,763 532,876 532,1102 337,1214 141,1102 141,876" fill="url(#goalie)"/>
  </svg>
  <div class="abs about">
    <div class="about-kicker">WHO WE ARE</div>
    <h2 class="about-title">ABOUT BRAMWORTH HOCKEY<br><span>DEVELOPMENT</span></h2>
    <div class="about-rule"></div>
    <p class="about-copy">Lorem ipsum dolor sit amet, consectetur adipiscing elit, sed do eiusmod tempor incididunt ut labore et dolore magna aliqua. Ut enim ad minim veniam, quis nostrud exercitation ullamco laboris nisi ut aliquip ex ea commodo consequat. Duis aute irure dolor in reprehenderit in voluptate velit.</p>
    <a class="btn-ink about-btn" href="#">LEARN MORE</a>
  </div>

  <!-- SEASON SPLIT -->
  <section class="abs season">
    <svg class="abs" style="left:0;top:0" width="1200" height="602" viewBox="0 0 1200 602" role="img" aria-label="Hockey players skating, tinted blue for winter and dark for spring">
      <defs>
        <linearGradient id="winterTint" x1="0" y1="0" x2="0" y2="1">
          <stop offset="0" stop-color="#1ba9ec"/>
          <stop offset="1" stop-color="#0f9ae0"/>
        </linearGradient>
        <linearGradient id="springTint" x1="0" y1="0" x2="1" y2="1">
          <stop offset="0" stop-color="#1b2c42"/>
          <stop offset="0.5" stop-color="#2f4a64"/>
          <stop offset="1" stop-color="#4d6a84"/>
        </linearGradient>
      </defs>
      <polygon points="0,2 607,66 607,538 0,602" fill="url(#winterTint)"/>
      <polygon points="607,66 1200,2 1200,602 607,538" fill="url(#springTint)"/>
    </svg>
    <div class="season-block" style="left:94px;top:216px">
      <h3 class="season-title">WINTER PROGRAMS</h3>
      <div class="season-rule"></div>
      <p class="season-copy">Lorem ipsum dolor sit amet, consectetur adipi-<br>scing elit, sed do eiusmod tempor</p>
      <a class="btn-outline season-btn" href="#">LEARN MORE</a>
    </div>
    <div class="season-block" style="left:684px;top:224px">
      <h3 class="season-title">SPRING PROGRAMS</h3>
      <div class="season-rule"></div>
      <p class="season-copy">Lorem ipsum dolor sit amet, consectetur adipi-<br>scing elit, sed do eiusmod tempor</p>
      <a class="btn-outline season-btn" href="#">LEARN MORE</a>
    </div>
  </section>

  <!-- SPRING PROGRAM CARDS -->
  <h2 class="section-title" style="top:1867px"><span>SPIRNG</span> PROGRAMS</h2>
  <div class="section-rule" style="top:1914px"></div>

  <div class="program-card" style="left:0;width:296px;background:linear-gradient(160deg,#b9cfe2 0%,#6f8fb0 50%,#2b4a6c 100%)" role="img" aria-label="Youth players skating in colourful jerseys">
    <div class="caption"><div class="caption-title">LOREM IPSUM DOLOR SIT</div><a class="caption-link" href="#">VIEW DETAILS</a></div>
  </div>
  <div class="program-feature" role="img" aria-label="Goalie in net, tinted blue">
    <div class="feature-body">
      <div class="feature-title">SED UT PERSPICIATIS</div>
      <p class="feature-copy">Lorem ipsum dolor sit amet, consectetur adipiscing elit, sed do eiusmod tem</p>
      <a class="btn-outline feature-btn" href="#">LEARN MORE</a>
    </div>
  </div>
  <div class="program-card" style="left:602px;width:299px;background:linear-gradient(160deg,#d6e2ec 0%,#8aa6c0 50%,#35567a 100%)" role="img" aria-label="Player in white jersey skating with the puck">
    <div class="caption"><div class="caption-title">LOREM IPSUM DOLOR SIT</div><a class="caption-link" href="#">VIEW DETAILS</a></div>
  </div>
  <div class="program-card" style="left:905px;width:295px;background:linear-gradient(160deg,#6b89a8 0%,#2f4f73 55%,#1a3050 100%)" role="img" aria-label="Goalie defending against an attacking player">
    <div class="caption"><div class="caption-title">LOREM IPSUM DOLOR SIT</div><a class="caption-link" href="#">VIEW DETAILS</a></div>
  </div>

  <!-- TOURNAMENTS -->
  <div class="abs tournament-bg"></div>
  <h2 class="section-title" style="top:2423px"><span>LATEST</span> TOURNAMENT</h2>
  <div class="section-rule" style="top:2470px"></div>

  <svg class="abs" style="left:74px;top:2668px" width="24" height="42" viewBox="0 0 24 42" aria-label="Previous"><polyline points="20,4 6,21 20,38" fill="none" stroke="#1fb0ec" stroke-width="5"/></svg>
  <svg class="abs" style="left:1134px;top:2668px" width="24" height="42" viewBox="0 0 24 42" aria-label="Next"><polyline points="4,4 18,21 4,38" fill="none" stroke="#1fb0ec" stroke-width="5"/></svg>

  <article class="tournament-card" style="left:126px">
    <div class="photo" role="img" aria-label="Player spraying ice in a dark arena" style="background:radial-gradient(circle at 45% 55%,#2f7fd0 0%,#14345e 50%,#0a1628 100%)"></div>
    <h3 class="t-title">LOREM TOURNAMENT</h3>
    <p class="t-copy">Lorem ipsum dolor sit amet, consectetur adipiscing elit, sed do eiusmod tempor incididunt ut labore et dolore</p>
    <a class="t-btn" href="#">LEARN MORE</a>
  </article>
  <article class="tournament-card" style="left:458px">
    <div class="photo" role="img" aria-label="Player lifting a championship trophy" style="background:linear-gradient(160deg,#2a4a78 0%,#5f7fa8 50%,#c9d3de 100%)"></div>
    <h3 class="t-title">LOREM TOURNAMENT</h3>
    <p class="t-copy">Lorem ipsum dolor sit amet, consectetur adipiscing elit, sed do eiusmod tempor incididunt ut labore et dolore</p>
    <a class="t-btn" href="#">LEARN MORE</a>
  </article>
  <article class="tournament-card" style="left:795px">
    <div class="photo" role="img" aria-label="Game action on the ice in a lit arena" style="background:linear-gradient(180deg,#0f1c30 0%,#3a4f6c 55%,#b8c7d6 100%)"></div>
    <h3 class="t-title">LOREM TOURNAMENT</h3>
    <p class="t-copy">Lorem ipsum dolor sit amet, consectetur adipiscing elit, sed do eiusmod tempor incididunt ut labore et dolore</p>
    <a class="t-btn" href="#">LEARN MORE</a>
  </article>

  <!-- FOOTER -->
  <svg class="abs" style="left:0;top:2990px" width="1200" height="357" viewBox="0 0 1200 357" aria-hidden="true">
    <polygon points="0,0 1200,30 1200,357 0,357" fill="#0f1c2e"/>
    <polygon points="600,28 1200,6 1200,52" fill="#1fb0ec"/>
  </svg>
  <div class="abs footer-brand">BRAMWORTH<br>HOCKEY<br>DEVELOPMENT</div>
  <p class="abs footer-about">Lorem ipsum dolor sit amet, consectetur adipiscing elit, sed do eiusmod te</p>

  <div class="footer-sep" style="left:490px"></div>
  <div class="footer-sep" style="left:713px"></div>
  <div class="footer-sep" style="left:906px"></div>

  <div class="footer-mark" style="left:490px"></div>
  <div class="footer-col" style="left:512px">
    <h4>NAVIGATION</h4>
    <ul><li>Home</li><li>Spring Program</li><li>Summer Programs</li><li>Tournaments</li></ul>
  </div>
  <div class="footer-mark" style="left:713px"></div>
  <div class="footer-col" style="left:731px">
    <h4>RESOURCES</h4>
    <ul><li>Winter</li><li>Blogs</li><li>Contact Us</li></ul>
  </div>
  <div class="footer-mark" style="left:906px"></div>
  <div class="footer-col" style="left:933px">
    <h4>FOLLLOW US</h4>
  </div>
  <a class="social" href="#" aria-label="Social profile one" style="left:933px"></a>
  <a class="social" href="#" aria-label="Social profile two" style="left:968px"></a>
  <a class="social" href="#" aria-label="Social profile three" style="left:1002px"></a>
  <a class="social" href="#" aria-label="Social profile four" style="left:1036px"></a>

  <div class="abs copyright">© 2022 <a href="#">Bramworth Hockey Development</a> All Rights Reserved</div>
</div>
</body>
</html>
```